Stationery design for law/Property/finance business

We need stationery design for a Law/Property/Finance business called Stonebridge. Logo is attached.
we require a letterhead and with compliments slip.
Would like to see a very simple professional design using the colours of the logo and offset against Charcoal colours. Maybe a charcoal band for header and footer with logo and details appearing in it? Former letterhead attached for examples.
we require the project to be provided in word, pdf and jpeg format.
we require the following details on the stationery:
Cairns Phone: 07 41592036
Weipa Phone: 07 41357904
Mobile: 0427 915 384
Fax: 07 41836257
email: admin@stonebridgeholdings.com.au
ABN 52 304 781 619

```html
<!DOCTYPE html>
<html lang="en">
<head>
<meta charset="utf-8">
<title>Stonebridge Stationery</title>
<link href="https://fonts.googleapis.com/css2?family=Roboto+Condensed:wght@400;700&family=Roboto:wght@400;700&display=swap" rel="stylesheet">
<style>
  :root {
    --teal: #2bb49c;
    --blue: #2a73b6;
    --ink: #1f1f1f;
    --paper: #ffffff;
    --backdrop: #e8e8e4;
  }
  * { margin: 0; padding: 0; box-sizing: border-box; }
  html, body { width: 1189px; height: 1200px; overflow: hidden; }
  body { background: var(--backdrop); position: relative; font-family: "Roboto", Arial, sans-serif; color: var(--ink); }

  .sheet { position: absolute; left: 277px; width: 635px; background: var(--paper); box-shadow: 0 2px 8px rgba(0,0,0,0.12); }
  .letterhead { top: 29px; height: 825px; }
  .slip { top: 872px; height: 299px; }

  .brand { position: absolute; display: flex; align-items: center; gap: 10px; }
  .brand-dot { width: 22px; height: 22px; border-radius: 50%; background: var(--teal); }
  .brand-name { font-family: "Roboto", Arial, sans-serif; font-weight: 700; color: var(--blue); letter-spacing: -0.5px; }
  .letterhead .brand { left: 81px; top: 108px; }
  .letterhead .brand-name { font-size: 36px; }
  .slip .brand { right: 28px; top: 80px; }
  .slip .brand-name { font-size: 40px; }

  .contacts { position: absolute; text-align: right; line-height: 1.25; }
  .contacts .label { color: var(--teal); }
  .contacts .group { margin-bottom: 6px; }
  .contacts .line { display: flex; justify-content: flex-end; align-items: center; gap: 4px; }
  .icon { width: 9px; height: 9px; background: var(--teal); border-radius: 1px; display: inline-block; position: relative; }
  .icon::after { content: ""; position: absolute; left: 2px; top: 2px; width: 5px; height: 4px; background: #fff; border-radius: 1px; }
  .letterhead .contacts { right: 78px; top: 55px; font-size: 11.5px; }
  .slip .contacts { right: 28px; top: 158px; font-size: 12.8px; }
  .slip .icon { width: 10px; height: 10px; }

  .body-copy { position: absolute; left: 81px; top: 222px; width: 475px; font-family: "Roboto Condensed", "Arial Narrow", sans-serif; font-size: 11.4px; line-height: 18.9px; }
  .body-copy p { margin-bottom: 18.9px; }
  .body-copy p.spaced { margin-top: 18px; }

  .footer-band { position: absolute; left: 0; bottom: 0; width: 635px; }
</style>
</head>
<body>

<section class="sheet letterhead">
  <div class="brand"><span class="brand-dot"></span><span class="brand-name">Stonebridge</span></div>

  <div class="contacts">
    <div class="group">
      <div><span class="label">Cairns Phone:</span> 07 41592036</div>
      <div><span class="label">Weipa Phone:</span> 07 41357904</div>
    </div>
    <div class="group">
      <div class="line">0427 915 384 <span class="icon"></span></div>
      <div class="line">07 41836257 <span class="icon"></span></div>
      <div class="line">admin@stonebridgeholdings.com.au <span class="icon"></span></div>
    </div>
    <div><span class="label">ABN</span> 52 304 781 619</div>
  </div>

  <div class="body-copy">
    <p>Lorem Ipsum is simply dummy text of the printing and typesetting industry. Lorem Ipsum has been the industry’s standard dummy text ever since the 1500s, when an unknown printer took a galley of type and scrambled it to make a type specimen book. It has survived not only five centuries, but also the leap into electronic typesetting, remaining essentially unchanged. It was popularised in the 1960s with the release of Marlowe sheets containing Lorem Ipsum passages, and more recently with desktop publishing software like Quillset Composer including versions of Lorem Ipsum.</p>
    <p>It is a long established fact that a reader will be distracted by the readable content of a page when looking at its layout. The point of using Lorem Ipsum is that it has a more-or-less normal distribution of letters, as opposed to using ’Content here, content here’, making it look like readable English. Many desktop publishing packages and web page editors now use Lorem Ipsum as their default model text, and a search for ’lorem ipsum’ will uncover many web sites still in their infancy. Various versions have evolved over the years, sometimes by accident, sometimes on purpose (injected humour and the like).</p>
    <p class="spaced">Contrary to popular belief, Lorem Ipsum is not simply random text. It has roots in a piece of classical Latin literature from 45 BC, making it over 2000 years old. Edwin Hartwell, a Latin professor at Ashcombe College in Vermont, looked up one of the more obscure Latin words, consectetur, from a Lorem Ipsum passage, and going through the cites of the word in classical literature, discovered the undoubtable source. Lorem Ipsum comes from sections 1.10.32 and 1.10.33 of "de Finibus Bonorum et Malorum" structures, to generate Lorem Ipsum which looks reasonable. The generated Lorem Ipsum is therefore always free from repetition, injected humour, or non-characteristic words etc.</p>
  </div>

  <svg class="footer-band" width="635" height="27" viewBox="0 0 635 27" aria-hidden="true">
    <polygon points="0,9 392,9 386,27 0,27" fill="var(--teal)"/>
    <polygon points="398,0 635,0 635,27 389,27" fill="var(--blue)"/>
  </svg>
</section>

<section class="sheet slip">
  <div class="brand"><span class="brand-dot"></span><span class="brand-name">Stonebridge</span></div>

  <div class="contacts">
    <div class="group">
      <div><span class="label">Cairns Phone:</span> 07 41592036</div>
      <div><span class="label">Weipa Phone:</span> 07 41357904</div>
    </div>
    <div class="group">
      <div class="line">0427 915 384 <span class="icon"></span></div>
      <div class="line">07 41836257 <span class="icon"></span></div>
      <div class="line">admin@stonebridgeholdings.com.au <span class="icon"></span></div>
    </div>
    <div><span class="label">ABN</span> 52 304 781 619</div>
  </div>

  <svg class="footer-band" width="635" height="25" viewBox="0 0 635 25" aria-hidden="true">
    <polygon points="0,7 381,7 374,25 0,25" fill="var(--teal)"/>
    <polygon points="389,0 635,0 635,25 379,25" fill="var(--blue)"/>
  </svg>
</section>

</body>
</html>
```